Easter & Summer School Dance Camps

I need two flyers one for Easter camps and one for summer school
We are a performing arts and dance academy

I want a double sided flyers one side summer school one side easter camp
Updates

Please make these flyers appeal to young dancers and performers - eye catching up to date Added Tuesday, March 1, 2016

Target Market(s)

Young children and teenagers

Industry/Entity Type

School

Font styles to use
Serif
Sans Serif

Requirements
Must have
• bright colourful

```html
<!DOCTYPE html>
<html lang="en">
<head>
<meta charset="utf-8">
<title>Brightstep Easter Dance Camp</title>
<link rel="stylesheet" href="https://fonts.googleapis.com/css2?family=Chewy&family=Arimo:wght@700&display=swap">
<style>
  :root {
    --stripe-light: #c9e2b3;
    --stripe-dark: #b3d597;
    --white: #ffffff;
    --pink: #ec4f9c;
    --orange: #f39200;
    --green: #86d060;
    --ink: #1a1a1a;
    --display: "Chewy", "Comic Sans MS", "Chalkboard SE", cursive;
    --body: "Arimo", "Arial", "Helvetica", sans-serif;
  }
  * { margin: 0; padding: 0; box-sizing: border-box; }
  html, body { width: 1200px; height: 564px; overflow: hidden; }
  .flyer {
    position: relative;
    width: 1200px;
    height: 564px;
    overflow: hidden;
    background: repeating-linear-gradient(-45deg,
      var(--stripe-light) 0 22px,
      var(--stripe-dark) 22px 44px);
    font-family: var(--body);
    font-weight: 700;
  }
  .shapes { position: absolute; inset: 0; }
  .badge-text { position: absolute; text-align: center; font-weight: 700; white-space: nowrap; }
  .brand {
    left: 40px; top: 122px; width: 330px;
    display: flex; align-items: center; justify-content: center; gap: 12px;
    font-size: 52px; line-height: 1; color: var(--ink);
  }
  .brand-dot { width: 28px; height: 28px; border-radius: 50%; background: var(--pink); }
  .workshop-title {
    left: 486px; top: 88px; width: 240px;
    font-family: var(--display);
    font-weight: 400;
    font-size: 40px; line-height: 1.15; color: var(--green);
    letter-spacing: 2px; transform: rotate(7deg);
  }
  .price {
    left: 862px; top: 118px; width: 300px;
    font-size: 38px; line-height: 1.2; color: var(--orange);
    transform: rotate(-3deg);
  }
  .dates {
    left: 33px; top: 364px; width: 230px;
    font-size: 23px; line-height: 1.17; color: var(--orange);
  }
  .venue {
    left: 928px; top: 345px; width: 260px;
    font-size: 20px; line-height: 1.22; color: var(--pink);
  }
  .tagline {
    position: absolute; left: 250px; top: 282px; width: 700px;
    text-align: center;
    font-family: var(--display);
    font-size: 38px; line-height: 50px; color: var(--white);
    letter-spacing: 1px;
  }
  .tagline .fun { color: var(--pink); }
  .tagline .fresh { color: var(--green); }
  .tagline .funky { color: var(--orange); }
  .booking {
    left: 360px; top: 466px; width: 480px;
    font-size: 19px; line-height: 1.3; color: var(--green);
  }
</style>
</head>
<body>
<main class="flyer">
  <svg class="shapes" width="1200" height="564" viewBox="0 0 1200 564" aria-hidden="true">
    <g fill="var(--white)">
      <ellipse cx="205" cy="158" rx="198" ry="132"/>
      <ellipse cx="606" cy="140" rx="152" ry="122"/>
      <ellipse cx="1012" cy="165" rx="178" ry="118"/>
      <ellipse cx="148" cy="420" rx="142" ry="112"/>
      <ellipse cx="1058" cy="420" rx="148" ry="122"/>
      <rect x="345" y="448" width="510" height="92" rx="46"/>
    </g>
    <g fill="none" stroke-width="3.5" stroke-dasharray="14 9">
      <ellipse cx="205" cy="158" rx="182" ry="118" stroke="var(--pink)"/>
      <ellipse cx="606" cy="140" rx="138" ry="108" stroke="var(--green)"/>
      <ellipse cx="1012" cy="165" rx="162" ry="104" stroke="var(--orange)"/>
      <ellipse cx="148" cy="420" rx="128" ry="98" stroke="var(--orange)"/>
      <ellipse cx="1058" cy="420" rx="134" ry="108" stroke="var(--pink)"/>
      <rect x="358" y="460" width="484" height="68" rx="34" stroke="var(--green)"/>
    </g>
  </svg>

  <div class="badge-text brand"><span class="brand-dot"></span>Brightstep</div>

  <h1 class="badge-text workshop-title">WEST END<br>WORKSHOP</h1>

  <p class="badge-text price">30 per day/<br>55 for both</p>

  <p class="badge-text dates">Tuesday 5 &amp; 6<br>April 2016<br>8 - 16 years<br>1-4pm</p>

  <p class="badge-text venue">Venue<br>The Parish Hall<br>of St Aldric<br>Elmford<br>KT9 4ZZ</p>

  <p class="tagline">Our Easter dance camps are <span class="fun">fun,</span><br><span class="fresh">fresh</span> and <span class="funky">funky</span>, mixed together<br>with a little musical theatre!</p>

  <p class="badge-text booking">Email brightstepdance@gmail<br>to book or text 07700900461</p>
</main>
</body>
</html>
```